CarWrap Varlo Kestrel K4M1 for a bouncy castle rental in Germany ("Leaping Domes Wendbach...

Dear ArtRally Community,

We operate a bouncy castle rental service in Crailsheim ("Springwelt Tauberfeld"), Germany. Customers have the option to rent bouncy castles for self-pickup. However, a portion of our customers also prefer to book a full-service package, which includes us traveling to the customer's location to set up, operate, and dismantle the bouncy castles on-site. In addition to bouncy castles, we also offer XXL outdoor games and fun food. For delivery purposes, we operate a Varlo Kestrel, which we would like to have wrapped with branding.

Vehicle:
Varlo Kestrel 2020 K4M1

Design Focus & Requirements:
- We are a startup and cannot yet afford a full vehicle wrap. Therefore, please focus the design on the blue highlighted areas as shown in the file "Focus Area for CarWrap.pdf". Note: The blue color is used solely to indicate the designated design areas - it is not a color requirement.
- Lettering and design elements may also extend beyond the blue areas.
- Both sides (left & right) should be designed, with focus on the highlighted areas.
- Front and rear of the vehicle may also include lettering/design elements.

Mandatory Design Elements:
- Logo must be included (see provided vector files)
- Website URL: springwelt-tauberfeld.de
- Slogan: "Rent Bouncy Castles" (German for "Rent Bouncy Castles")
- No phone number or address required
- Our Bouncy Castle flag ship is our "pirate ship Bouncy Castle"

Color & Branding:
- Please use the color palette from the provided logo vector files only
- Our Proud Main Color is Yellow. With Black and Magenta as Secondary Color.
- Reference file: "Colors Main and Secondary"
- Further references available on our website: https://springwelt-tauberfeld. de

Provided Files:
- Logos, fonts, images, and vector files of various products - all may be used
- Target design file: "Varlo Kestrel CarWrap Target file.ai" - please submit your final design adapted to this file

Technical Requirements:
- Final file format: AI (adapted from provided target file)
- Color mode: CMYK
- Resolution: minimum 300 DPI for any raster elements

For more information please let us know.

Target Market(s)

- easy to read while driving

Font styles to use
Serif
Other font styles liked:
• Our Fonts as in files provided

Requirements
Must have
• - Our logo, "Rent bouncy castles"
Nice to have
• Some colorful elements, we would like to be recognized very easily :-)
Should not have
• No full area car wrap (we can't afford that)

```html
<!DOCTYPE html>
<html lang="de">
<head>
<meta charset="utf-8">
<title>Springwelt Tauberfeld – Van Wrap</title>
<link rel="stylesheet" href="https://fonts.googleapis.com/css2?family=Montserrat:wght@700;800&family=Kaushan+Script&display=swap">
<style>
  :root{
    --bg:#ffffff;
    --body:#ffffff;
    --line:#2b2b2d;
    --trim:#5b5b5e;
    --tyre:#3a3a3c;
    --glass:#c8c9cb;
    --tail:#c8202a;
    --yellow:#f7d400;
    --yellow-deep:#c9a800;
    --black:#111111;
    --magenta:#e0245e;
    --white:#ffffff;
  }
  html,body{margin:0;padding:0;background:var(--bg);overflow:hidden;}
  .wrap-sheet{width:1200px;height:1127px;display:block;}
  .van-body{fill:var(--body);stroke:var(--line);stroke-width:3;}
  .van-trim{fill:var(--trim);}
  .van-glass{fill:var(--glass);stroke:var(--line);stroke-width:6;}
  .van-dark{fill:var(--line);}
  .van-panel-line{fill:none;stroke:var(--line);stroke-width:2;}
  .van-soft-line{fill:none;stroke:#d4d4d6;stroke-width:2;}
  .tyre{fill:var(--tyre);stroke:#1f1f20;stroke-width:6;}
  .rim{fill:#4a4a4d;stroke:#222;stroke-width:4;}
  .hub{fill:#7a7a7d;stroke:#222;stroke-width:3;}
  .tail-light{fill:var(--tail);stroke:var(--line);stroke-width:3;}
  .tail-lens{fill:#e6e6e7;}
  .banner-yellow{fill:url(#yellowWash);}
  .photo-area{fill:url(#photoWash);}
  .photo-bubble{fill:#f3f1ee;stroke:var(--magenta);stroke-width:6;}
  .photo-bubble-dash{fill:none;stroke:var(--magenta);stroke-width:4;stroke-dasharray:14 10;}
  .brand-dot{fill:var(--black);}
  .brand-name{font-family:"Montserrat",sans-serif;font-weight:800;fill:var(--black);text-anchor:middle;letter-spacing:1px;}
  .slogan{font-family:"Kaushan Script",cursive;fill:var(--black);text-anchor:middle;font-size:38px;}
  .url-pill{fill:var(--black);}
  .url-text{font-family:"Montserrat",sans-serif;font-weight:700;fill:var(--white);font-size:19px;text-anchor:middle;}
  .url-icon{fill:none;stroke:var(--white);stroke-width:2;}
</style>
</head>
<body>
<svg class="wrap-sheet" viewBox="0 0 1988 1867" xmlns="http://www.w3.org/2000/svg">
  <defs>
    <linearGradient id="yellowWash" x1="0" y1="0" x2="1" y2="1">
      <stop offset="0" stop-color="#fbe04a"/>
      <stop offset="0.55" stop-color="#f7d400"/>
      <stop offset="1" stop-color="#d9b700"/>
    </linearGradient>
    <linearGradient id="photoWash" x1="0" y1="0" x2="0" y2="1">
      <stop offset="0" stop-color="#8a8f92"/>
      <stop offset="0.45" stop-color="#b8703a"/>
      <stop offset="1" stop-color="#3fa34a"/>
    </linearGradient>

    <g id="vanSide">
      <path class="van-body" d="M75,640 L85,525 Q100,482 250,452 L320,432 L560,205 Q700,110 920,102 L1790,102 Q1830,112 1836,165 L1860,460 L1880,640 L1900,735 L1895,760 L1400,770 L500,772 L230,780 L55,760 L45,680 Z"/>
      <path class="van-trim" d="M48,665 L80,628 L1880,620 L1900,735 L1895,760 L1400,770 L500,772 L230,780 L55,760 Z"/>
      <path fill="var(--body)" d="M512,712 L1380,706 L1380,748 L512,752 Z"/>
      <path class="van-dark" d="M230,760 Q240,590 362,590 Q485,590 500,760 Z"/>
      <path class="van-dark" d="M1390,752 Q1400,595 1527,595 Q1655,595 1665,752 Z"/>
      <path class="van-glass" d="M310,505 L560,240 L580,246 L365,440 Z" style="fill:#3a3a3d"/>
      <path class="van-glass" d="M480,290 L722,248 L716,400 Q700,458 560,480 L458,492 Z"/>
      <path class="van-dark" d="M430,380 Q440,350 480,355 L495,500 Q490,512 460,508 Q425,500 428,470 Z"/>
      <path fill="#9c9c9f" d="M458,428 L490,430 L492,495 L460,495 Z"/>
      <path class="van-panel-line" d="M115,545 L110,520 Q180,480 260,478 L215,560 Q150,572 115,565 Z" style="fill:#e9e9ea"/>
      <rect class="van-dark" x="662" y="490" width="78" height="10" rx="4"/>
      <circle cx="704" cy="564" r="6" fill="#888"/>
      <path class="van-panel-line" d="M762,122 L762,745 M1230,104 L1222,745"/>
      <path class="van-soft-line" d="M760,162 L1755,160 M770,488 L1660,460 M420,560 Q520,600 760,575 L1780,510"/>
      <rect x="532" y="720" width="85" height="14" fill="none" stroke="var(--line)" stroke-width="2"/>
      <path class="tail-light" d="M1805,450 Q1830,432 1848,445 L1852,630 L1808,630 Z"/>
      <path class="tail-lens" d="M1815,470 Q1828,455 1835,470 L1838,590 L1817,585 Z"/>
      <circle class="tyre" cx="362" cy="762" r="112"/>
      <circle class="rim" cx="362" cy="762" r="78"/>
      <circle class="hub" cx="362" cy="762" r="18"/>
      <circle class="tyre" cx="1527" cy="762" r="112"/>
      <circle class="rim" cx="1527" cy="762" r="78"/>
      <circle class="hub" cx="1527" cy="762" r="18"/>
    </g>

    <clipPath id="bannerTop">
      <path d="M825,210 L1725,210 Q1745,212 1745,240 L1745,372 Q1720,412 1650,436 L815,445 Q800,440 802,420 L812,232 Q815,212 825,210 Z"/>
    </clipPath>
    <clipPath id="bannerBottom">
      <path d="M268,1123 L1160,1125 Q1175,1130 1177,1150 L1187,1338 Q1187,1358 1168,1360 L340,1352 Q272,1340 243,1300 L245,1152 Q248,1125 268,1123 Z"/>
    </clipPath>
  </defs>

  <!-- left side of the van -->
  <use href="#vanSide"/>
  <g class="banner banner--left" clip-path="url(#bannerTop)">
    <rect class="banner-yellow" x="795" y="205" width="960" height="245"/>
    <rect class="photo-area" x="1230" y="205" width="525" height="245" role="img" aria-label="Foto der Piratenschiff-Hüpfburg mit Kapitänsfigur"/>
    <circle class="photo-bubble" cx="1335" cy="282" r="65" role="img" aria-label="Hüpfburg mit Rutsche"/>
    <circle class="photo-bubble-dash" cx="1335" cy="282" r="76"/>
    <circle class="photo-bubble" cx="1393" cy="375" r="52" role="img" aria-label="Bunte Hüpfburg" style="stroke:#58c6c8"/>
    <circle class="photo-bubble" cx="1312" cy="388" r="42" role="img" aria-label="Kleine Hüpfburg"/>
  </g>
  <g class="brand brand--left">
    <circle class="brand-dot" cx="1037" cy="262" r="26"/>
    <text class="brand-name" x="1037" y="322" font-size="30">SPRINGWELT</text>
    <text class="brand-name" x="1037" y="347" font-size="17" letter-spacing="4">TAUBERFELD</text>
    <text class="slogan" x="1037" y="385">"Rent Bouncy Castles"</text>
    <rect class="url-pill" x="895" y="404" width="280" height="30" rx="7"/>
    <circle class="url-icon" cx="911" cy="419" r="7"/>
    <text class="url-text" x="1043" y="426">springwelt-tauberfeld.de</text>
  </g>

  <!-- right side of the van -->
  <use href="#vanSide" transform="translate(1985,918) scale(-1,1)"/>
  <g class="banner banner--right" clip-path="url(#bannerBottom)">
    <rect class="banner-yellow" x="240" y="1118" width="955" height="248"/>
    <rect class="photo-area" x="240" y="1118" width="517" height="248" role="img" aria-label="Foto der Dschungel-Hüpfburg mit großer Gorilla-Figur"/>
    <circle class="photo-bubble" cx="655" cy="1200" r="62" role="img" aria-label="Hüpfburg mit Rutsche"/>
    <circle class="photo-bubble-dash" cx="655" cy="1200" r="73"/>
    <circle class="photo-bubble" cx="595" cy="1295" r="50" role="img" aria-label="Bunte Hüpfburg" style="stroke:#58c6c8"/>
    <circle class="photo-bubble" cx="676" cy="1302" r="42" role="img" aria-label="Kleine Hüpfburg"/>
  </g>
  <g class="brand brand--right">
    <circle class="brand-dot" cx="955" cy="1178" r="26"/>
    <text class="brand-name" x="955" y="1238" font-size="30">SPRINGWELT</text>
    <text class="brand-name" x="955" y="1263" font-size="17" letter-spacing="4">TAUBERFELD</text>
    <text class="slogan" x="955" y="1301">"Rent Bouncy Castles"</text>
    <rect class="url-pill" x="814" y="1320" width="280" height="30" rx="7"/>
    <circle class="url-icon" cx="830" cy="1335" r="7"/>
    <text class="url-text" x="962" y="1342">springwelt-tauberfeld.de</text>
  </g>
</svg>
</body>
</html>
```